Business Card for Wholesale Comapany
Pelvo Goods
Business Card for Wholesale Comapany - Construction
Creative Brief
Professional
Mark Tilney
Chief Sales Officer
8142-C Marlow Ridge Boulevard #310 Houston, TX. 77031-2287
mtilney@pelvogoods.example
www.pelvogoods.example
Your design can be for one or both sides of the card, I do not have a preference. I just completed the contest for my logo design and as soon as the .ai file is sent to me I will forward. But, for the time being, you can find my logo at http://www.brakenstudio.example/drafts/display/contest/519274/draft/7a1c04be92d3f65e08b1c7a94f3e2d60b815937.
rkanto41q rkanto41q
Here is the .ai file for the logo, so hopefully this will make it easier for you designs. Also, some great designs have been submitted and here are some items I have gravitated to: 1. I am going to want rounded corners. 2. I like the idea of having a 2 sided card. 3. On the back, almost all designs have come in black. I would like to see another color used, or make a statement with design on a white background. 4. Don't be too heavily skewed to the professional type of card. Thanks
VelMar VelMar
What font did you use sir?

```html
<!DOCTYPE html>
<html lang="en">
<head>
<meta charset="utf-8">
<title>Pelvo Goods – Business Card</title>
<link href="https://fonts.googleapis.com/css2?family=Oswald:wght@400;600&family=Roboto+Condensed:ital,wght@0,400;1,400&display=swap" rel="stylesheet">
<style>
  :root {
    --bg: #d9d9d9;
    --card-white: #f7f7f7;
    --card-black: #0d0d0d;
    --gold: #a8875a;
    --ink: #1e1e1e;
    --muted: #555555;
    --light: #e6e6e6;
  }
  html, body {
    margin: 0;
    width: 1200px;
    height: 946px;
    overflow: hidden;
    background: var(--bg);
  }
  .canvas {
    position: relative;
    width: 1200px;
    height: 946px;
  }
  .card {
    position: absolute;
    left: 250px;
    width: 700px;
    height: 400px;
    border-radius: 28px;
    box-shadow: 0 10px 30px rgba(0,0,0,0.18);
    overflow: hidden;
  }
  .card--back { top: 56px; background: var(--card-black); }
  .card--front { top: 490px; background: var(--card-white); }

  .brand {
    display: flex;
    align-items: center;
    gap: 14px;
    font-family: "Oswald", sans-serif;
    font-weight: 600;
    color: var(--gold);
    letter-spacing: 1px;
  }
  .brand__mark {
    width: 34px;
    height: 34px;
    background: var(--gold);
  }
  .card--back .brand {
    position: absolute;
    left: 50%;
    top: 44%;
    transform: translate(-50%, -50%);
    font-size: 56px;
  }
  .social {
    position: absolute;
    right: 40px;
    bottom: 30px;
    display: flex;
    gap: 28px;
    font-family: "Roboto Condensed", sans-serif;
    font-size: 15px;
    color: var(--light);
  }
  .social__item { display: flex; align-items: center; gap: 8px; }
  .social__square { width: 18px; height: 18px; background: var(--light); }

  .card--front .brand {
    position: absolute;
    left: 44px;
    top: 52px;
    font-size: 40px;
  }
  .details {
    position: absolute;
    left: 300px;
    top: 54px;
    display: flex;
    flex-direction: column;
    gap: 34px;
  }
  .row {
    display: flex;
    align-items: center;
    gap: 16px;
  }
  .row__icon { width: 34px; height: 34px; fill: var(--ink); flex: none; }
  .row__rule { width: 3px; align-self: stretch; background: var(--ink); }
  .row__text {
    font-family: "Roboto Condensed", sans-serif;
    font-size: 19px;
    line-height: 1.35;
    color: var(--ink);
    letter-spacing: 0.5px;
  }
  .person__name {
    font-family: "Oswald", sans-serif;
    font-weight: 600;
    font-size: 30px;
    letter-spacing: 1.5px;
    line-height: 1.1;
    text-transform: uppercase;
  }
  .person__title {
    font-style: italic;
    color: var(--muted);
    font-size: 17px;
  }
</style>
</head>
<body>
<main class="canvas">
  <section class="card card--back" aria-label="Card back">
    <div class="brand"><span class="brand__mark"></span>Pelvo Goods</div>
    <div class="social">
      <span class="social__item"><span class="social__square"></span>/pelvogoods</span>
      <span class="social__item"><span class="social__square"></span>/pelvogoods</span>
    </div>
  </section>

  <section class="card card--front" aria-label="Card front">
    <div class="brand"><span class="brand__mark"></span>Pelvo Goods</div>
    <div class="details">
      <div class="row">
        <svg class="row__icon" viewBox="0 0 24 24" aria-hidden="true">
          <circle cx="12" cy="7" r="5"/>
          <path d="M2 23c0-6 4.5-9 10-9s10 3 10 9z"/>
        </svg>
        <span class="row__rule"></span>
        <div class="row__text">
          <div class="person__name">Mark Tilney</div>
          <div class="person__title">Managing Director</div>
        </div>
      </div>
      <div class="row">
        <svg class="row__icon" viewBox="0 0 24 24" aria-hidden="true">
          <path d="M12 1a8 8 0 0 0-8 8c0 6 8 14 8 14s8-8 8-14a8 8 0 0 0-8-8zm0 11a3 3 0 1 1 0-6 3 3 0 0 1 0 6z"/>
        </svg>
        <span class="row__rule"></span>
        <div class="row__text">8142-C Marlow Ridge Blvd<br>Houston, TX 77031</div>
      </div>
      <div class="row">
        <svg class="row__icon" viewBox="0 0 24 24" aria-hidden="true">
          <path d="M12 1a11 11 0 1 0 0 22 11 11 0 0 0 0-22zm8.9 10h-4c-.1-3-.8-5.6-1.9-7.5A9 9 0 0 1 20.9 11zM12 3c1.2 1.5 2.2 4.5 2.3 8H9.7C9.8 7.5 10.8 4.5 12 3zM9 3.5C7.9 5.4 7.2 8 7.1 11h-4A9 9 0 0 1 9 3.5zM3.1 13h4c.1 3 .8 5.6 1.9 7.5A9 9 0 0 1 3.1 13zM12 21c-1.2-1.5-2.2-4.5-2.3-8h4.6c-.1 3.5-1.1 6.5-2.3 8zm3 -.5c1.1-1.9 1.8-4.5 1.9-7.5h4a9 9 0 0 1-5.9 7.5z"/>
        </svg>
        <span class="row__rule"></span>
        <div class="row__text">014 552 7301<br>mtilney@pelvogoods.example<br>www.pelvogoods.example</div>
      </div>
    </div>
  </section>
</main>
</body>
</html>
```